Occupational Medical Billing and Coding Business needs Postcard

Medical billing and coding business needs marketing postcard to send to target audience of orthopaedic surgeons who practice medicine in California Workers' Compensation industry. These doctors treat injured workers and/or provide medical-legal evaluations and reports for the courts to settle the injured worker's claim. This is a highly specialized area of medical billing and coding. It is extremely complicated and can be very frustrating for doctors and their staff who do not understand the system. I would encourage the designers to check out my website: www.CorvaleHealthClaims.com
I want something bright and colorful that makes bold statements. It has to get their attention. My suggestions for bold statements include:
1) QMEs! Are your bills compliant with DWC's view? We make sure your complexity factors are maximized as well as compliant.
2) We collected over $ 462,000 just in second bill review (SBR) appeals alone and that's just one orthopaedic surgeon! Imagine what we can do for you!

I uploaded a word document with some information about the services I offer. The company logo is also there. Let me know if you need it in another format. The items with the asterisk (**) must be in the postcard.

Thank you so much!

Corvale Health Claims

Target Market(s)

Orthopaedic Surgeons who treat injured workers in California

Font styles to use
Sans Serif

Colors

Designer to choose colors to be used in the design.

Requirements
Must have
• Expert Billing and Coding Services for:
• QME - AME - IME Evaluations
• Radiology - MRI/CT Scans
• Orthopaedic Surgery
• Certified Coders on Staff
• Electronic Claim Submission
• Payment within 15 days
• It's important to spell orthopaedic with the "A" after the "P" as it is an acknowledgment of the origins of the practice and will attract a doctor with higher education.

```html
<!DOCTYPE html>
<html lang="en">
<head>
<meta charset="utf-8">
<title>Corvale Health Claims Postcard</title>
<link rel="stylesheet" href="https://fonts.googleapis.com/css2?family=Open+Sans:wght@400;600;700;800&display=swap">
<style>
:root{
  --blue:#2b7fc6;
  --blue-dark:#1d5f9c;
  --navy:#1b3558;
  --peach:#f9cfae;
  --peach-light:#fde3cf;
  --white:#ffffff;
  --bg:#e9ebee;
  --ink:#33424f;
}
*{margin:0;padding:0;box-sizing:border-box}
html,body{width:1200px;height:2248px;overflow:hidden;background:var(--bg);font-family:"Open Sans",Arial,sans-serif;color:var(--ink)}
.card{position:absolute;left:40px;width:1120px;height:770px;background:var(--white);overflow:hidden;box-shadow:0 6px 24px rgba(0,0,0,.18)}
.front{top:290px}
.back{top:1170px}
.shapes{position:absolute;inset:0}
.abs{position:absolute}

/* front */
.headline{left:36px;top:28px;width:600px;font-size:38px;line-height:1.18;font-weight:700;color:var(--blue)}
.brand{right:36px;top:40px;text-align:right;font-size:30px;font-weight:700;color:var(--navy);line-height:1.1;width:260px}
.office-photo{left:560px;top:150px;width:560px;height:460px;background:linear-gradient(135deg,#f4f5f6 0%,#dfe3e7 45%,#c9ced4 100%)}
.services{left:34px;top:222px;width:520px;color:var(--white)}
.services h2{font-size:23px;font-weight:700;margin-bottom:12px}
.services ul{list-style:none}
.services li{font-size:18px;line-height:1.3;padding-left:26px;position:relative;margin-bottom:2px}
.services li .sub{display:block}
.services li::before{content:"\2713";position:absolute;left:0;top:0;font-weight:700}
.call{left:40px;top:618px;font-size:50px;font-weight:600;color:var(--blue);white-space:nowrap}
.call strong{font-weight:800}
.footer-links{left:0;top:700px;width:1120px;height:70px;display:flex;align-items:center;gap:150px;padding-left:40px;color:var(--white);font-size:21px}
.footer-links span{display:flex;align-items:center;gap:10px}

/* back */
.collections{left:34px;top:40px;width:500px;color:var(--white)}
.collections h2{font-size:25px;font-weight:700;margin-bottom:16px}
.collections ul{list-style:none}
.collections li{font-size:17px;line-height:1.4;padding-left:24px;position:relative;margin-bottom:18px}
.collections li::before{content:"\2713";position:absolute;left:0;top:0;font-weight:700}
.contact{left:0;top:545px;width:420px;height:225px;background:var(--peach-light);padding:22px 34px}
.contact h3{font-size:22px;font-weight:700;color:var(--navy);margin-bottom:12px}
.contact p{font-size:18px;line-height:1.55;color:var(--ink);display:flex;align-items:center;gap:10px}
.stamp{right:40px;top:40px;width:110px;height:130px;border:2px solid #b9c0c7}
.address-line{left:640px;width:420px;height:2px;background:#b9c0c7}
</style>
</head>
<body>

<section class="card front">
  <svg class="shapes" width="1120" height="770" viewBox="0 0 1120 770">
    <polygon points="0,0 760,0 690,195 0,195" fill="var(--peach)"/>
    <polygon points="0,200 690,200 535,610 0,610" fill="var(--blue)"/>
    <polygon points="700,200 720,200 565,610 545,610" fill="var(--blue-dark)"/>
    <polygon points="728,200 740,200 585,610 573,610" fill="var(--navy)"/>
  </svg>
  <div class="abs office-photo" role="img" aria-label="Bright modern medical office interior with desk and chairs" style="clip-path:polygon(30% 0,100% 0,100% 100%,0 100%)"></div>
  <svg class="shapes" width="1120" height="770" viewBox="0 0 1120 770">
    <rect x="0" y="610" width="1120" height="90" fill="var(--peach)"/>
    <polygon points="700,610 760,610 730,700 670,700" fill="var(--white)" opacity=".8"/>
    <rect x="0" y="700" width="1120" height="70" fill="var(--blue)"/>
  </svg>

  <h1 class="abs headline">Medical Billing &amp; Collections for California Workers' Compensation Providers</h1>
  <div class="abs brand">Corvale Health Claims</div>

  <div class="abs services">
    <h2>Expert Billing and Coding Services for:</h2>
    <ul>
      <li>QME – AME – IME Evaluations <span class="sub">Treatment – Primary/Secondary Physician</span></li>
      <li>Radiology – MRI/CT Scans <span class="sub">Electrodiagnostic Studies</span></li>
      <li>Orthopaedic Surgery <span class="sub">Ambulatory Surgery Centers</span></li>
      <li>Certified Coders on Staff</li>
      <li>Electronic Claim Submission</li>
      <li>Payment within 15 days</li>
      <li>Over 25 Years Experience in Workers' Comp</li>
    </ul>
  </div>

  <div class="abs call">Call Today: <strong>714.555.0142</strong></div>

  <div class="abs footer-links">
    <span><svg width="24" height="18" viewBox="0 0 24 18"><rect x="1" y="1" width="22" height="16" rx="2" fill="none" stroke="#fff" stroke-width="2"/><polyline points="1,2 12,10 23,2" fill="none" stroke="#fff" stroke-width="2"/></svg>info@CorvaleHealthClaims.com</span>
    <span><svg width="22" height="22" viewBox="0 0 22 22"><circle cx="11" cy="11" r="9.5" fill="none" stroke="#fff" stroke-width="2"/><ellipse cx="11" cy="11" rx="4" ry="9.5" fill="none" stroke="#fff" stroke-width="1.6"/><line x1="1.5" y1="11" x2="20.5" y2="11" stroke="#fff" stroke-width="1.6"/></svg>www.CorvaleHealthClaims.com</span>
  </div>
</section>

<section class="card back">
  <svg class="shapes" width="1120" height="770" viewBox="0 0 1120 770">
    <polygon points="0,0 580,0 470,545 0,545" fill="var(--blue)"/>
    <polygon points="592,0 612,0 482,660 462,660" fill="var(--navy)"/>
    <polygon points="620,0 632,0 495,700 483,700" fill="var(--blue-dark)"/>
  </svg>

  <div class="abs collections">
    <h2>We also provide Collection Services:</h2>
    <ul>
      <li>Expert Denial Management: Timely filing of SBR and IBR Appeals – Collected over $462,000 just in second bill review appeals. This is an example of ONE orthopaedic surgeon to date. Imagine what we can do for you!</li>
      <li>Don't let insurance companies "zero-out" your QME and AME bills. We get your medical-legal bills paid including penalty, interest and costs associated with the effort to collect.</li>
    </ul>
  </div>

  <div class="abs contact">
    <h3>Contact Us</h3>
    <p><svg width="16" height="16" viewBox="0 0 16 16"><path d="M3 1l3 3-2 2c1 2 3 4 5 5l2-2 3 3-2 3C6 15 1 10 1 3z" fill="var(--navy)"/></svg>714.555.0142</p>
    <p><svg width="16" height="12" viewBox="0 0 16 12"><rect x="1" y="1" width="14" height="10" fill="none" stroke="var(--navy)" stroke-width="1.6"/><polyline points="1,1 8,7 15,1" fill="none" stroke="var(--navy)" stroke-width="1.6"/></svg>info@CorvaleHealthClaims.com</p>
    <p><svg width="16" height="16" viewBox="0 0 16 16"><circle cx="8" cy="8" r="7" fill="none" stroke="var(--navy)" stroke-width="1.6"/><line x1="1" y1="8" x2="15" y2="8" stroke="var(--navy)" stroke-width="1.4"/></svg>www.CorvaleHealthClaims.com</p>
  </div>

  <div class="abs stamp"></div>
  <div class="abs address-line" style="top:380px"></div>
  <div class="abs address-line" style="top:440px"></div>
  <div class="abs address-line" style="top:500px"></div>
  <div class="abs address-line" style="top:560px"></div>
</section>

</body>
</html>
```